Broschüre für Konzepte rund um Immobilien
Zielgruppe
Wir sind ein junges, dynamisches Team und unterstützen Kunden mit individuellen, abgestimmten Konzepten rund um Ihre Immobilie - daher suchen wir ein hochwertiges Design, unsere Zielgruppe liegt Wert auf was neues, nicht das was jeder hat.
Aufgabenstellung
Die Farben und das Layout sollen von der Homepage übernommen werden www.k7-zelt.de..
Den Text entnehmen Sie der angehängten Datei. Bilder, Anordnungen und sonstiges überlasse ich Ihren kreativen Geist! DIN A5 Querformat - Bilder und Texte müssen in einer sehr hohen Auflösung umsetzbar sein!

```html
<!DOCTYPE html>
<html lang="de">
<head>
<meta charset="utf-8">
<title>K7ZELT Broschüre</title>
<link href="https://fonts.googleapis.com/css2?family=Inter:wght@300;400;600;700&display=swap" rel="stylesheet">
<style>
  :root{
    --navy:#1b2538;
    --white:#ffffff;
    --ink:#2a3346;
    --text-light:#d3d8e1;
    --paper:#ffffff;
  }
  *{margin:0;padding:0;box-sizing:border-box}
  html,body{width:849px;height:1200px;overflow:hidden;background:var(--paper)}
  body{position:relative;font-family:"Inter",Arial,sans-serif;color:var(--white)}
  .spread{position:absolute;left:77px;width:694px;height:244px;overflow:hidden}
  .spread-cover{top:36px}
  .spread-intro{top:325px}
  .spread-steps{top:614px}
  .spread-finish{top:903px}
  .panel{position:absolute;top:0;height:100%}
  .navy{background:var(--navy)}
  .photo{position:absolute;top:0;height:100%}
  .brand{position:absolute;font-weight:400;font-size:13px;letter-spacing:.5px;color:#c9ccd3;display:flex;align-items:center;gap:5px;white-space:nowrap}
  .brand-dot{width:7px;height:7px;border-radius:50%;background:#c9ccd3}
  .contact{position:absolute;left:0;width:347px;top:220px;text-align:center;font-size:5.2px;font-weight:400;color:var(--text-light);white-space:nowrap}
  .headline span{position:absolute;color:var(--ink);white-space:nowrap;line-height:1}
  .headline .light{font-weight:300;font-size:11px}
  .headline .bold{font-weight:700;font-size:14px}
  .copy{position:absolute;font-size:4.7px;line-height:8.8px;font-weight:300;color:var(--text-light)}
  .step-title{position:absolute;font-size:8.5px;line-height:10.5px;font-weight:300;color:var(--white);white-space:nowrap}
  .step-title b{font-weight:700;color:var(--white)}
  .sub-title{position:absolute;font-size:5px;line-height:8.8px;font-weight:700;color:var(--white)}

  .photo-cover{background:
    radial-gradient(ellipse 38% 30% at 38% 78%,#59647a 0%,rgba(89,100,122,0) 100%),
    radial-gradient(ellipse 40% 22% at 75% 70%,#7e8698 0%,rgba(126,134,152,0) 100%),
    radial-gradient(ellipse 22% 28% at 32% 22%,#cfcbc6 0%,rgba(207,203,198,0) 100%),
    linear-gradient(180deg,#f3f2ef 0%,#e9e6e2 55%,#d9d4cc 85%,#c9c2b6 100%)}
  .photo-family{background:
    radial-gradient(ellipse 50% 32% at 50% 50%,#8c8e93 0%,rgba(140,142,147,0) 100%),
    radial-gradient(ellipse 18% 20% at 72% 45%,#b68f6c 0%,rgba(182,143,108,0) 100%),
    radial-gradient(ellipse 70% 25% at 50% 82%,#d8cdbd 0%,rgba(216,205,189,0) 100%),
    linear-gradient(180deg,#f5f4f2 0%,#ecebe8 45%,#d7cfc3 75%,#b99a78 100%)}
  .photo-livingroom-blue{background:
    radial-gradient(ellipse 80% 16% at 55% 66%,#354877 0%,rgba(53,72,119,0) 100%),
    radial-gradient(ellipse 40% 25% at 60% 22%,#f4f6f8 0%,rgba(244,246,248,0) 100%),
    linear-gradient(180deg,#dfe4ea 0%,#cfd6de 50%,#3e4f7a 70%,#8e6e50 88%,#a4825f 100%)}
  .photo-plan{background:
    radial-gradient(ellipse 60% 30% at 50% 72%,#e6e7e8 0%,rgba(230,231,232,0) 100%),
    radial-gradient(ellipse 40% 40% at 55% 18%,#c7a97c 0%,rgba(199,169,124,0) 100%),
    linear-gradient(180deg,#7d6a52 0%,#a6947a 35%,#d4d2cd 65%,#b8bbbf 100%)}
  .photo-bath{background:
    radial-gradient(ellipse 30% 12% at 28% 73%,#c9c7c2 0%,rgba(201,199,194,0) 100%),
    radial-gradient(ellipse 20% 40% at 8% 60%,#8a6540 0%,rgba(138,101,64,0) 100%),
    radial-gradient(ellipse 35% 15% at 35% 88%,#8a6b4a 0%,rgba(138,107,74,0) 100%),
    linear-gradient(180deg,#727476 0%,#5f6264 40%,#55575a 70%,#3a3b3d 100%)}
  .photo-lounge{background:
    radial-gradient(ellipse 45% 18% at 55% 68%,#7b7c7e 0%,rgba(123,124,126,0) 100%),
    radial-gradient(ellipse 25% 35% at 20% 45%,#b9c2a8 0%,rgba(185,194,168,0) 100%),
    radial-gradient(ellipse 25% 45% at 88% 45%,#c8bfb3 0%,rgba(200,191,179,0) 100%),
    linear-gradient(180deg,#ececea 0%,#e2e2df 40%,#a9a9a7 65%,#a98562 85%,#8e6a48 100%)}
</style>
</head>
<body>

<section class="spread spread-cover">
  <div class="panel navy" style="left:0;width:347px">
    <div class="brand" style="left:140px;top:186px"><span class="brand-dot"></span>K7ZELT</div>
    <p class="contact">K7ZELT • Lindenweg 14 • 56000 Musterstadt • Telefon: 01234-567890 • info@k7-zelt.de</p>
  </div>
  <div class="photo photo-cover" role="img" aria-label="Vater liegt auf einem Teppich und hebt seine kleine Tochter in die Luft" style="left:347px;width:347px"></div>
  <div class="headline">
    <span class="light" style="left:580px;top:15px">WIR PLANEN</span>
    <span class="light" style="left:564px;top:29px">UND GESTALTEN</span>
    <span class="bold" style="left:580px;top:42px">IHREN</span>
    <span class="light" style="left:548px;top:58px">PERSÖNLICHEN</span>
    <span class="bold" style="left:561px;top:70px">LEBENS(T)RAUM</span>
  </div>
  <div class="panel navy" style="left:600px;top:156px;width:94px;height:59px">
    <div class="brand" style="left:17px;top:23px;font-size:11px"><span class="brand-dot" style="width:6px;height:6px"></span>K7ZELT</div>
  </div>
</section>

<section class="spread spread-intro">
  <div class="photo photo-family" role="img" aria-label="Familie mit zwei Kindern liegt lächelnd auf einem hellen Teppich im Wohnzimmer" style="left:0;width:347px"></div>
  <div class="panel navy" style="left:347px;width:248px">
    <p class="copy" style="left:17px;top:96px;width:98px">Wir möchten, dass Sie glücklich sind. Dass Sie von uns Ihr persönliches Konzept erhalten und in ein Haus ziehen, welches die Grundlage für ein freudvolles und lebenslustiges Leben bietet. Ein Haus, welches gerade im Inneren, Ihnen, Ihrer Persönlichkeit und den Bedürfnissen aller Bewohner entspricht.</p>
    <p class="copy" style="left:124px;top:96px;width:102px">Mit individuellen Gesamtkonzepten ist es K7ZELT ein Bedürfnis, Ihren Lebens(t)raum so auf Ihre Persönlichkeit und Bedürfnisse abzustimmen, dass Ihr persönliches Glück und Freude beim Wohnen gleich mit einziehen.<br><br>Hand in Hand wird durch kurze Kommunikationswege, enge Zusammenarbeit mit den einzelnen Fachplanern und der gemeinsamen Betreuung Ihr Hausprojekt optimal geplant.</p>
  </div>
  <div class="photo photo-livingroom-blue" role="img" aria-label="Helles Wohnzimmer mit blauem Sofa und großem Sprossenfenster" style="left:595px;width:99px"></div>
</section>

<section class="spread spread-steps">
  <div class="photo photo-plan" role="img" aria-label="Hände zeigen mit Stift auf einen Grundrissplan" style="left:0;width:116px"></div>
  <div class="panel navy" style="left:116px;width:231px">
    <div class="step-title" style="left:8px;top:80px"><b>SCHRITT 1</b><br>DAS AUSFÜHRLICHE<br>VORGESPRÄCH</div>
    <p class="copy" style="left:8px;top:120px;width:96px">Die Bemusterung für die Hausbaudetails steht an – unser Berater von K7ZELT trifft sich mit Ihnen zum Gespräch, bei dem Sie sich kennenlernen. Sie berichten wie Sie derzeit leben und Sie erzählen von Ihren Wünschen und vor allem, wie Sie sich Ihr zukünftiges Zuhause vorstellen. Natürlich wird hierbei jeder Raum, sowie Ihre eigenen Stilwünsche unter die Lupe genommen.</p>
    <p class="sub-title" style="left:116px;top:120px;width:110px">IHR ZUKÜNFTIGES HAUS<br>IN GUTEN HÄNDEN</p>
    <p class="copy" style="left:116px;top:146px;width:98px">Im Anschluss des Gespräches werden sämtliche Ideen und Konzepten an die jeweiligen Partnerfirmen übergeben. Jetzt sind alle entscheidenden Details in guten Händen, um von nun an die optimale Planung für Sie angehen zu können.</p>
  </div>
  <div class="photo photo-bath" role="img" aria-label="Modernes Badezimmer mit grauen Fliesen, Holzwaschtisch und Glasdusche" style="left:347px;width:223px">
    <div class="step-title" style="left:124px;top:80px"><b>SCHRITT 2</b><br>IHR PERSÖNLICHES<br>FUSSBODEN KONZEPT</div>
    <p class="copy" style="left:124px;top:120px;width:94px;color:#e4e4e4">Egal ob Fliesen, Parkett oder Teppichboden – ein Fußboden bildet das bestimmende „Fundament“ für das Raumgefühl in Ihren Räumen. Fußböden sollten so gewählt sein, dass man sich lange darüber freuen kann und sich anschließend nicht ärgert. Aber es ist erneut wichtig, dass die Auswahl zur Raumwirkung und den Möbelvorstellungen passt – hier ist Erfahrung gefragt!</p>
  </div>
  <div class="panel navy" style="left:570px;width:124px">
    <div class="step-title" style="left:8px;top:80px"><b>SCHRITT 3</b><br>IHR PERSÖNLICHES<br>BAD KONZEPT</div>
    <p class="copy" style="left:8px;top:120px;width:98px">Wer sein Bad nach eigenen Wünschen gestalten möchte, hat heute die Qual der Wahl. Entscheiden Sie sich für die Wellness-Oase oder doch lieber das funktionale Bad mit bedacht auf das Alter? Warum nicht beides? Wir nennen es das Bad zum Wohlfühlen, ausgerichtet auf Ihre Wünsche und Bedürfnisse.</p>
  </div>
</section>

<section class="spread spread-finish">
  <div class="panel navy" style="left:0;width:231px">
    <div class="step-title" style="left:17px;top:80px"><b>SCHRITT 4</b><br>IHRE PLANUNG<br>IST FERTIG</div>
    <p class="copy" style="left:17px;top:120px;width:98px">Sie treffen sich nach ca. 4 Wochen wieder. Gemeinsam mit unserem Berater gehen Sie nun zu unseren Partnerfirmen das gesamte Gestaltungskonzept durch und stimmen Details nochmals ab. Inhaltliche und organisatorische Fragen für die Umsetzung werden geklärt.</p>
    <div class="step-title" style="left:124px;top:80px"><b>SCHRITT 5</b><br>IN VERBINDUNG<br>BLEIBEN</div>
    <p class="copy" style="left:124px;top:120px;width:98px">Nun haben Sie alle Möglichkeiten, Ihre individuelle Raumgestaltung umzusetzen. K7ZELT unterstützt Sie weiterhin gerne im Bereich Möbel- und Küchenkonzepte. Wann und wie Sie Empfehlungen oder das gesamte Konzept verwirklichen, entscheiden Sie selbst…</p>
  </div>
  <div class="photo photo-lounge" role="img" aria-label="Großzügiges helles Wohnzimmer mit grauer Sofalandschaft, Holzboden und offener Küche" style="left:231px;width:463px"></div>
</section>

</body>
</html>
```